Harborline Optical -Window Poster (Optometrist)

We are an optometry practice and we need a poster for a new store promotion for our window highlighting we now also sell 2 pairs of glasses as a package deal. The size will be 1300mm width x 1900mm height

The artwork will be displayed as a fabric banner in our shop window. We have 7 other banners with different services our business provides. The words needs to standout for passers by and the cars stopped at the traffic lights out front of our business. We already have signs with our logos phone number etc. so we won't need them included in the poster.

It would need to include the following information.

Two pair packages now available*

*Conditions apply
Updates

The artwork will be displayed as a fabric banner in our shop window. We have 7 other banners with different services our business provides. The words needs to standout for passers by and the cars stopped at the traffic lights out front of our business. We already have signs with our logos phone number etc. so we won't need them included in the poster. Thank you for your work it's amazing Added Saturday, February 18, 2017

The artwork will be displayed as a fabric banner in our shop window. We have 7 other banners with different services our business provides. The words needs to standout for passers by and the cars stopped at the traffic lights out front of our business. We already have signs with our logos phone number etc. so we won't need them included in the poster. Added Saturday, February 18, 2017

Target Market(s)

Cars driving past and stopped at traffic lights outside our store.

Industry/Entity Type

Optician

Requirements
Must have
• Poster must say:
• Two pair packages now available*
• *Conditions apply

```html
<!DOCTYPE html>
<html lang="en">
<head>
<meta charset="utf-8">
<title>Harborline Optical – Two Pair Packages Window Poster</title>
<link rel="stylesheet" href="https://fonts.googleapis.com/css2?family=Outfit:wght@400;700;800&display=swap">
<style>
  :root {
    --paper: #f7f7f8;
    --ink: #141414;
    --frame-orange: #f06a2a;
    --frame-lime: #c6dc5a;
    --frame-teal: #2bb3d6;
    --frame-pink: #ec8fb8;
    --poster-width: 822px;
    --poster-height: 1200px;
  }
  html, body {
    margin: 0;
    padding: 0;
    overflow: hidden;
    background: var(--paper);
  }
  .poster {
    position: relative;
    width: var(--poster-width);
    height: var(--poster-height);
    overflow: hidden;
    background: var(--paper);
    font-family: "Outfit", sans-serif;
    color: var(--ink);
  }
  .poster__photo {
    position: absolute;
    left: 0;
    top: 0;
    width: 822px;
    height: 1060px;
    background:
      linear-gradient(105deg, var(--paper) 0%, rgba(247,247,248,0.85) 22%, rgba(247,247,248,0) 55%),
      linear-gradient(180deg, rgba(247,247,248,0) 70%, var(--paper) 100%),
      linear-gradient(160deg,
        #f3c3a6 0%,
        var(--frame-orange) 24%,
        var(--frame-lime) 42%,
        var(--frame-teal) 60%,
        var(--frame-pink) 80%,
        #f6dbe8 100%);
    opacity: 0.85;
  }
  .poster__headline {
    position: absolute;
    left: 49px;
    top: 826px;
    margin: 0;
    font-weight: 800;
    font-size: 69px;
    line-height: 77px;
    letter-spacing: -0.8px;
  }
  .poster__headline sup {
    font-size: 34px;
    line-height: 0;
    vertical-align: 30px;
  }
  .poster__conditions {
    position: absolute;
    left: 49px;
    top: 1130px;
    margin: 0;
    font-weight: 700;
    font-size: 17px;
  }
</style>
</head>
<body>
  <main class="poster">
    <div class="poster__photo" role="img" aria-label="Photograph of four stacked spectacle frames in orange, lime green, turquoise and pink, receding diagonally from top left across a white background"></div>
    <h1 class="poster__headline">Two Pair<br>Packages<br>NOW Available<sup>*</sup></h1>
    <p class="poster__conditions">*Conditions Apply.</p>
  </main>
</body>
</html>
```